Album Jacket for young indie musicians in AFRICA #2 Baraka, Tumaini And Neema (Peace, Love And Unity)

We are ZEBO SOUND (zebo-sound.example), a music label for young African musicians living in a slum. I would like to ask you to design our new album's cover jacket. The title is Baraka, Tumaini And Neema (it means "Peace, Love And Unity" in Swahili. I entrust you whether you use English words in the design or not.), musician name is Daniel Okwaro. Add our label logo (we have various versions and can provide). I attached Daniel Okwaro's photo also. Please listen to the music of the album on Soundcloud. https://audiovault.example/tags/danielokwaro

Target Market(s)

International. not only African music funs.

Requirements
Must have
• Title, Musician's name, ZEBO SOUND Logo
• In order to upload to iTunes, I require the final that the following conditions are met.
• 1400 x 1400 pixels
• JPG file type
• 72 - 300dpi (300dpi is the best)
• Less than 25mb
• RGB color scheme (not CMYK)
Nice to have
• His music is something bright and little funny. Please express the tone of music in the design.
Should not have
• African traditional image

```html
<!DOCTYPE html>
<html lang="en">
<head>
<meta charset="utf-8">
<title>Baraka, Tumaini and Neema — Daniel Okwaro</title>
<link rel="stylesheet" href="https://fonts.googleapis.com/css2?family=Indie+Flower&family=Amatic+SC:wght@700&display=swap">
<style>
  :root {
    --page: #ffffff;
    --wash-pink: #e6407a;
    --wash-red: #d9283e;
    --wash-orange: #f6a02a;
    --wash-yellow: #fbe98a;
    --wash-cream: #fbf2dc;
    --wash-blue: #2f3fbf;
    --wash-violet: #8a3fb8;
    --accent: #e8305a;
    --ink: #1a1a1a;
    --white: #ffffff;
  }
  * { margin: 0; padding: 0; box-sizing: border-box; }
  html, body { width: 1200px; height: 900px; overflow: hidden; background: var(--page); }
  .canvas { position: relative; width: 1200px; height: 900px; background: var(--page); }
  .cover {
    position: absolute; left: 147px; top: 0; width: 900px; height: 900px; overflow: hidden;
    background:
      radial-gradient(ellipse 420px 380px at 560px 430px, var(--wash-cream) 0%, rgba(251,242,220,0) 70%),
      radial-gradient(ellipse 500px 360px at 760px 120px, var(--wash-orange) 0%, rgba(246,160,42,0) 75%),
      radial-gradient(ellipse 520px 500px at 80px 120px, var(--wash-pink) 0%, rgba(230,64,122,0) 75%),
      radial-gradient(ellipse 360px 300px at 280px 200px, var(--wash-red) 0%, rgba(217,40,62,0) 75%),
      radial-gradient(ellipse 420px 380px at 0px 900px, var(--wash-blue) 0%, rgba(47,63,191,0) 75%),
      radial-gradient(ellipse 360px 300px at 160px 700px, var(--wash-violet) 0%, rgba(138,63,184,0) 75%),
      linear-gradient(135deg, var(--wash-pink) 0%, var(--wash-yellow) 55%, var(--wash-orange) 100%);
  }
  .portrait {
    position: absolute; left: 450px; top: 60px; width: 450px; height: 840px;
    border-radius: 200px 200px 0 0;
    background: radial-gradient(ellipse 60% 55% at 55% 62%, #f47a2a 0%, #e8482c 55%, rgba(232,72,44,0) 100%);
    opacity: .9;
  }
  .title-frame {
    position: absolute; left: 23px; top: 38px; width: 488px; height: 702px;
    border: 3px solid rgba(255,255,255,.6); border-radius: 28px;
    background: rgba(255,255,255,.14);
  }
  .title {
    position: absolute; left: 23px; top: 88px; width: 488px; text-align: center;
    font-family: "Indie Flower", cursive; font-weight: 400; font-size: 92px; line-height: 124px;
    color: var(--white); text-shadow: 0 2px 6px rgba(0,0,0,.25);
  }
  .subtitle {
    position: absolute; left: 23px; top: 482px; width: 488px; text-align: center;
    font-family: "Amatic SC", sans-serif; font-weight: 700; font-size: 50px;
    color: var(--accent);
  }
  .divider { position: absolute; left: 58px; top: 561px; width: 412px; height: 3px; background: var(--accent); }
  .artist {
    position: absolute; left: 23px; top: 596px; width: 488px; text-align: center;
    font-family: "Amatic SC", sans-serif; font-weight: 700; font-size: 76px;
    color: var(--white); text-shadow: 0 3px 6px rgba(0,0,0,.35);
  }
  .label {
    position: absolute; left: 23px; top: 782px; width: 488px;
    display: flex; flex-direction: column; align-items: center;
  }
  .label-name {
    font-family: "Amatic SC", sans-serif; font-weight: 700; font-size: 68px; line-height: 1;
    color: var(--ink); letter-spacing: 2px;
  }
  .label-tagline {
    font-family: "Amatic SC", sans-serif; font-weight: 700; font-size: 30px; line-height: 1;
    color: var(--ink); margin-top: 6px;
  }
</style>
</head>
<body>
<div class="canvas">
  <section class="cover">
    <div class="portrait" role="img" aria-label="Photo of Daniel Okwaro smiling in a bright floral shirt"></div>
    <div class="title-frame"></div>
    <h1 class="title">Baraka,<br>Tumaini,<br>and Neema</h1>
    <p class="subtitle">Peace, Love and Unity</p>
    <div class="divider"></div>
    <h2 class="artist">Daniel Okwaro</h2>
    <div class="label">
      <span class="label-name">ZEBO SOUND</span>
      <span class="label-tagline">young voices, bright sounds</span>
    </div>
  </section>
</div>
</body>
</html>
```